Beautiful Web banner ad 300X250

i need an animated banner with graphics, to drive traffic to a website that focuses on architecturally significant homes in Toronto.

"cedar crest homes" logo should appear, and visuals. Call to action is "tour the latest homes"

http://danielwhitcombe.com

Number of Pages Required

1 page

Font styles to use
Sans Serif

Requirements
Must have
• the logo of my brand
Nice to have
• smart graphics, nice transitions, elegant

```html
<!DOCTYPE html>
<html lang="en">
<head>
<meta charset="utf-8">
<title>Cedar Crest Homes – 300x250 Banner Set</title>
<link href="https://fonts.googleapis.com/css2?family=Open+Sans:wght@300;400;700;800&display=swap" rel="stylesheet">
<style>
  :root {
    --board: #2a2a2a;
    --navy: #0b2266;
    --deep: #081845;
    --blue: #1d4ba8;
    --bright: #2f6fd8;
    --gold: #f4b22e;
    --ink: #0c1f4f;
    --white: #ffffff;
    --label: #f2f2f2;
    --shade: #0d1428;
  }
  html, body { margin: 0; padding: 0; overflow: hidden; }
  body {
    width: 1200px;
    height: 944px;
    background: var(--board);
    position: relative;
    font-family: "Open Sans", Arial, sans-serif;
  }
  .banner {
    position: absolute;
    width: 479px;
    height: 398px;
    display: block;
    box-shadow: 0 4px 14px rgba(0,0,0,.45);
  }
  .banner--a { left: 102px; top: 59px; }
  .banner--b { left: 620px; top: 58px; }
  .banner--c { left: 359px; top: 488px; }
  .banner-label { position: absolute; color: var(--label); font-size: 22px; font-weight: 400; }
  .banner-label--a { left: 124px; top: 470px; }
  .banner-label--b { left: 1068px; top: 470px; }
  .banner-label--c { left: 852px; top: 862px; }
  .size-note { position: absolute; left: 890px; top: 772px; color: var(--label); line-height: 1; }
  .size-note__dims { font-size: 46px; font-weight: 400; display: block; }
  .size-note__caption { font-size: 20px; font-weight: 400; display: block; margin-top: 6px; }
  .headline-bold { font-weight: 800; fill: var(--white); }
  .headline-light { font-weight: 400; fill: var(--white); }
  .site-name { font-weight: 300; fill: var(--white); }
  .tagline { font-weight: 300; fill: var(--white); }
  .cta-text { font-weight: 700; fill: var(--ink); }
</style>
</head>
<body>

<!-- Banner A -->
<svg class="banner banner--a" viewBox="0 0 300 250" aria-label="Cedar Crest Homes banner A">
  <defs>
    <linearGradient id="a-room" x1="0" y1="0" x2="0" y2="1">
      <stop offset="0" stop-color="#33466e"/>
      <stop offset=".22" stop-color="#7a7488"/>
      <stop offset=".36" stop-color="#e3a45e"/>
      <stop offset=".5" stop-color="#8c6440"/>
      <stop offset=".75" stop-color="#5a4230"/>
      <stop offset="1" stop-color="#2e241c"/>
    </linearGradient>
    <radialGradient id="a-lamp" cx=".55" cy=".55" r=".45">
      <stop offset="0" stop-color="#f0c58a" stop-opacity=".55"/>
      <stop offset="1" stop-color="#f0c58a" stop-opacity="0"/>
    </radialGradient>
    <linearGradient id="a-tower" x1="0" y1="0" x2="0" y2="1">
      <stop offset="0" stop-color="#2c4a8c"/>
      <stop offset=".45" stop-color="#a99a86"/>
      <stop offset=".8" stop-color="#d8a765"/>
      <stop offset="1" stop-color="#4b3a2a"/>
    </linearGradient>
    <linearGradient id="a-blue" x1="0" y1="0" x2="1" y2="1">
      <stop offset="0" stop-color="var(--bright)"/>
      <stop offset=".6" stop-color="var(--blue)"/>
      <stop offset="1" stop-color="var(--navy)"/>
    </linearGradient>
  </defs>
  <g role="img" aria-label="Photo: open living and dining room with floor-to-ceiling windows over the city at dusk">
    <rect width="300" height="250" fill="url(#a-room)"/>
    <rect width="300" height="250" fill="url(#a-lamp)"/>
  </g>
  <g role="img" aria-label="Photo: lit modern condo tower at twilight">
    <polygon points="0,0 82,0 48,88 0,94" fill="url(#a-tower)"/>
  </g>
  <polygon points="82,0 132,0 98,72 48,88" fill="var(--navy)"/>
  <polygon points="98,72 132,0 140,0 104,76" fill="var(--deep)"/>
  <polygon points="0,94 48,88 98,72 0,112" fill="var(--navy)"/>
  <polygon points="0,112 98,72 150,122 240,200 300,190 300,250 0,250" fill="url(#a-blue)"/>
  <polygon points="98,72 112,74 250,196 240,200" fill="var(--shade)"/>
  <text class="headline-bold" x="8" y="143" font-size="19.5">CEDAR</text>
  <text class="headline-light" x="8" y="163" font-size="18">CREST HOMES</text>
  <line x1="8" y1="170" x2="150" y2="170" stroke="var(--white)" stroke-width=".6" opacity=".75"/>
  <rect x="8" y="187" width="19" height="11" fill="var(--white)"/>
  <text class="site-name" x="31" y="198" font-size="17">danielwhitcombe.com</text>
  <text class="tagline" x="72" y="210" font-size="10.5">cedar crest homes</text>
  <rect x="6" y="223" width="150" height="19" fill="var(--gold)"/>
  <polygon points="12,227.5 20,232.5 12,237.5" fill="var(--navy)"/>
  <text class="cta-text" x="25" y="235.8" font-size="8.2">TOUR THE LATEST HOMES</text>
</svg>
<span class="banner-label banner-label--a">A</span>

<!-- Banner B -->
<svg class="banner banner--b" viewBox="0 0 300 250" aria-label="Cedar Crest Homes banner B">
  <defs>
    <linearGradient id="b-sky" x1="0" y1="0" x2="0" y2="1">
      <stop offset="0" stop-color="#1a40b4"/>
      <stop offset="1" stop-color="#3f7be0"/>
    </linearGradient>
    <linearGradient id="b-tower" x1="0" y1="0" x2="1" y2="0">
      <stop offset="0" stop-color="#c7cfdc"/>
      <stop offset=".35" stop-color="#8e97a6"/>
      <stop offset=".6" stop-color="#2c3038"/>
      <stop offset=".75" stop-color="#6b3b2e"/>
      <stop offset="1" stop-color="#3a241e"/>
    </linearGradient>
    <radialGradient id="b-glow" cx=".8" cy=".7" r=".4">
      <stop offset="0" stop-color="#e6a35a" stop-opacity=".55"/>
      <stop offset="1" stop-color="#e6a35a" stop-opacity="0"/>
    </radialGradient>
    <linearGradient id="b-room" x1="0" y1="0" x2="0" y2="1">
      <stop offset="0" stop-color="#cfd6e6"/>
      <stop offset=".35" stop-color="#6a6f9a"/>
      <stop offset=".55" stop-color="#c98c70"/>
      <stop offset=".7" stop-color="#3a3a48"/>
      <stop offset="1" stop-color="#1e1c22"/>
    </linearGradient>
    <linearGradient id="b-band" x1="0" y1="0" x2="1" y2="0">
      <stop offset="0" stop-color="var(--bright)"/>
      <stop offset="1" stop-color="var(--navy)"/>
    </linearGradient>
  </defs>
  <rect width="300" height="250" fill="url(#b-sky)"/>
  <g role="img" aria-label="Photo: glass-fronted mid-rise condo beside brick storefronts at dusk">
    <polygon points="132,62 198,18 236,0 300,0 300,186 136,196" fill="url(#b-tower)"/>
    <polygon points="132,62 198,18 236,0 300,0 300,186 136,196" fill="url(#b-glow)"/>
  </g>
  <g role="img" aria-label="Photo: living room with large corner windows at dusk">
    <polygon points="0,128 48,96 150,136 138,250 0,250" fill="url(#b-room)"/>
  </g>
  <polygon points="130,250 152,214 300,176 300,250" fill="url(#b-band)"/>
  <text class="headline-bold" x="6" y="40" font-size="31">CEDAR</text>
  <text class="headline-bold" x="7" y="63" font-size="17.5">CREST HOMES</text>
  <rect x="134" y="198" width="15" height="10" fill="var(--white)"/>
  <text class="site-name" x="152" y="208" font-size="13.5">danielwhitcombe.com</text>
  <rect x="143" y="224" width="150" height="19" fill="var(--gold)"/>
  <polygon points="149,228.5 157,233.5 149,238.5" fill="var(--navy)"/>
  <text class="cta-text" x="161" y="236.8" font-size="8.2">TOUR THE LATEST HOMES</text>
</svg>
<span class="banner-label banner-label--b">B</span>

<!-- Banner C -->
<svg class="banner banner--c" viewBox="0 0 300 250" aria-label="Cedar Crest Homes banner C">
  <defs>
    <linearGradient id="c-room" x1="0" y1="0" x2="1" y2="1">
      <stop offset="0" stop-color="#7a6a58"/>
      <stop offset=".5" stop-color="#a4774a"/>
      <stop offset="1" stop-color="#2a2420"/>
    </linearGradient>
    <linearGradient id="c-terrace" x1="0" y1="0" x2="0" y2="1">
      <stop offset="0" stop-color="#4d6eb4"/>
      <stop offset=".35" stop-color="#8a86a0"/>
      <stop offset=".55" stop-color="#c88a5c"/>
      <stop offset="1" stop-color="#2e2826"/>
    </linearGradient>
    <linearGradient id="c-house" x1="0" y1="0" x2="0" y2="1">
      <stop offset="0" stop-color="#2a55b8"/>
      <stop offset=".3" stop-color="#4e6aa8"/>
      <stop offset=".5" stop-color="#b8905e"/>
      <stop offset=".8" stop-color="#6c5a40"/>
      <stop offset="1" stop-color="#252620"/>
    </linearGradient>
    <radialGradient id="c-glow" cx=".6" cy=".45" r=".45">
      <stop offset="0" stop-color="#f2bf72" stop-opacity=".6"/>
      <stop offset="1" stop-color="#f2bf72" stop-opacity="0"/>
    </radialGradient>
    <linearGradient id="c-band" x1="0" y1="0" x2="1" y2="0">
      <stop offset="0" stop-color="var(--bright)"/>
      <stop offset="1" stop-color="var(--navy)"/>
    </linearGradient>
  </defs>
  <g role="img" aria-label="Photo: modern stacked townhouse block lit at night">
    <rect width="300" height="198" fill="url(#c-house)"/>
    <rect width="300" height="198" fill="url(#c-glow)"/>
  </g>
  <g role="img" aria-label="Photo: warm-lit interior with kitchen and lounge">
    <path d="M0,0 H110 Q96,35 92,70 H0 Z" fill="url(#c-room)"/>
  </g>
  <path d="M0,70 H92 Q90,97 91,124 H0 Z" fill="var(--blue)"/>
  <g role="img" aria-label="Photo: rooftop terrace lounge overlooking the city">
    <path d="M0,124 H91 Q93,162 104,198 H0 Z" fill="url(#c-terrace)"/>
  </g>
  <path d="M110,0 Q80,100 104,198" fill="none" stroke="var(--white)" stroke-width="2"/>
  <text class="headline-bold" x="4" y="96" font-size="19">CEDAR</text>
  <text class="headline-bold" x="5" y="113" font-size="10.5">CREST HOMES</text>
  <rect y="197" width="300" height="53" fill="url(#c-band)"/>
  <rect x="12" y="205" width="19" height="11" fill="var(--white)"/>
  <text class="site-name" x="35" y="217" font-size="17">danielwhitcombe.com</text>
  <rect x="145" y="226" width="147" height="19" fill="var(--gold)"/>
  <polygon points="151,230.5 159,235.5 151,240.5" fill="var(--navy)"/>
  <text class="cta-text" x="163" y="238.8" font-size="8">TOUR THE LATEST HOMES</text>
</svg>
<span class="banner-label banner-label--c">C</span>

<div class="size-note">
  <span class="size-note__dims">300x250</span>
  <span class="size-note__caption">Actual Size</span>
</div>

</body>
</html>
```